Upbeat Accouting Package Flyer

I am looking for a 1 page (front, or front and back) flyer that will become our marketing for our accounting services. We are looking for something a little different and we are catering to the small retail shop owners. We have 3 accounting packages we would like to display and then some add-ons. I have included our logo that must be included in the design. I have uploaded the accounting package information as well.
Target Market(s)
Small Retail Shop Owners
Industry/Entity Type
Accounting
Colors
Designer to choose colors to be used in the design.
Requirements
Must have
- A casual feel. We are not your typical accountants who are very professional and "stuffy". I want it to feel like we are all family.
Nice to have
- I would like to incorporate some sort of retail theme.
- We have a couple of taglines we like to use and it would be great if they could be included. They are "We know you CAN do the accounting, but do you WANT to?" and "We allow you to get back to what's important."
Should not have
- Typical stock accounting photos of people shaking hands, large office buildings, etc.

```html
<!DOCTYPE html>
<html lang="en">
<head>
<meta charset="utf-8">
<title>Keystead Tax and Accounting – Accounting Packages Flyer</title>
<link rel="stylesheet" href="https://fonts.googleapis.com/css2?family=Poppins:wght@600&family=Roboto:wght@400;500;700&family=Open+Sans:wght@400;600&display=swap">
<style>
  :root {
    --navy: #1b2b44;
    --navy-deep: #0f1a2c;
    --teal: #4fe0d2;
    --teal-text: #2fcfc0;
    --ink: #222222;
    --body: #333333;
    --band-grey: #8a8d8d;
    --page: #e9e9e7;
    --paper: #ffffff;
  }
  * { box-sizing: border-box; margin: 0; padding: 0; }
  html, body { width: 1200px; height: 1200px; overflow: hidden; background: var(--page); }
  .flyer {
    position: absolute; left: 200px; top: 40px;
    width: 800px; height: 1120px;
    background: var(--paper);
    box-shadow: 0 6px 24px rgba(0,0,0,.18);
    overflow: hidden;
  }
  .hero {
    position: absolute; left: 0; top: 0; width: 800px; height: 470px;
    background: linear-gradient(135deg, var(--navy) 0%, #24406a 55%, var(--navy-deep) 100%);
    border-bottom-right-radius: 40px;
  }
  .hero-photo {
    position: absolute; right: 0; top: 0; width: 460px; height: 470px;
    background: radial-gradient(circle at 55% 35%, rgba(79,224,210,.35) 0%, rgba(79,224,210,0) 40%),
                linear-gradient(160deg, #2a3d5c 0%, #1a2a44 100%);
    border-bottom-right-radius: 40px;
  }
  .hero-accent {
    position: absolute; left: 0; top: 466px; width: 800px; height: 6px;
    background: var(--teal);
  }
  .brand-bar {
    position: absolute; left: 0; top: 0; width: 520px; height: 125px;
    background: var(--paper);
    border-bottom-right-radius: 30px;
    border-bottom: 5px solid var(--teal);
    padding: 32px 0 0 50px;
  }
  .brand-name {
    font-family: "Poppins", sans-serif; font-weight: 600;
    font-size: 44px; color: var(--ink); letter-spacing: -1px; line-height: 1;
  }
  .brand-sub {
    font-family: "Poppins", sans-serif; font-weight: 600;
    font-size: 13px; color: var(--ink); letter-spacing: 1px; margin-top: 6px;
  }
  .headline {
    position: absolute; left: 50px; top: 190px;
    font-family: "Roboto", sans-serif; font-weight: 700;
    color: var(--paper); font-size: 30px; line-height: 1.35;
  }
  .headline .shout { color: var(--teal); font-size: 44px; }
  .section-title {
    position: absolute; left: 40px; top: 500px;
    font-family: "Roboto", sans-serif; font-weight: 700;
    font-size: 28px; line-height: 36px; color: var(--teal-text);
    padding-left: 16px; border-left: 8px solid var(--teal);
  }
  .col { position: absolute; }
  .col-left { left: 40px; top: 555px; width: 395px; }
  .col-right { left: 440px; top: 496px; width: 340px; }
  .package { margin-bottom: 22px; }
  .package-name {
    font-family: "Roboto", sans-serif; font-weight: 700; font-size: 23px; line-height: 28px;
    color: var(--teal-text); display: flex; align-items: center; gap: 8px;
  }
  .package-name .u { text-decoration: underline; }
  .package-name .note { color: var(--ink); font-size: 21px; }
  .package-icon { width: 22px; height: 22px; flex: none; }
  .features {
    list-style: none; margin: 8px 0 0 18px;
    font-family: "Open Sans", sans-serif; font-size: 11px; line-height: 17px; color: var(--body);
    white-space: nowrap;
  }
  .features li::before { content: "•"; color: var(--teal-text); margin-right: 7px; }
  .addons-title {
    font-family: "Roboto", sans-serif; font-weight: 700; font-size: 23px;
    color: var(--teal-text); text-decoration: underline; margin: 4px 0 12px;
  }
  .addons { display: grid; grid-template-columns: 145px 1fr; row-gap: 6px;
    font-family: "Roboto", sans-serif; font-size: 16px; white-space: nowrap; }
  .addon-label { font-weight: 700; color: var(--ink); }
  .addon-price { color: var(--teal-text); font-weight: 500; font-size: 18px; }
  .addon-price small { color: var(--ink); font-weight: 700; font-size: 13px; margin-left: 4px; }
  .call-band {
    position: absolute; left: 0; bottom: 0; width: 800px; height: 110px;
    background: var(--band-grey);
    border-top-left-radius: 30px;
    border-top: 6px solid var(--teal);
    padding: 34px 0 0 50px;
    font-family: "Roboto", sans-serif; font-size: 34px; color: var(--paper);
  }
</style>
</head>
<body>
<main class="flyer">
  <section class="hero">
    <div class="hero-photo" role="img" aria-label="Businessman holding a tablet with a glowing circuit-board brain above it"></div>
    <header class="brand-bar">
      <div class="brand-name">keystead</div>
      <div class="brand-sub">TAX AND ACCOUNTING INC.</div>
    </header>
    <h1 class="headline">
      We know you <span class="shout">CAN</span><br>
      Do the Accounting,<br>
      But Do You <span class="shout">WANT</span> to?
    </h1>
  </section>
  <div class="hero-accent"></div>

  <h2 class="section-title">Accounting Packages</h2>

  <div class="col col-left">
    <article class="package">
      <h3 class="package-name">
        <svg class="package-icon" viewBox="0 0 22 22"><circle cx="11" cy="11" r="9.5" fill="none" stroke="var(--teal-text)" stroke-width="2"/><circle cx="11" cy="11" r="3" fill="var(--teal-text)"/></svg>
        <span class="u">Develop</span>
      </h3>
      <ul class="features">
        <li>$300/mo when paid annually; $325/mo billed monthly</li>
        <li>CloudLedger Online subscription</li>
        <li>Free accounting setup</li>
        <li>Weekly transaction processing</li>
        <li>Monthly account reconciliation (up to 2 accounts)</li>
        <li>Monthly financial statements by the 15th of the month</li>
      </ul>
    </article>
    <article class="package">
      <h3 class="package-name">
        <svg class="package-icon" viewBox="0 0 22 22"><circle cx="11" cy="11" r="9.5" fill="none" stroke="var(--teal-text)" stroke-width="2"/><rect x="6" y="11" width="2.5" height="5" fill="var(--teal-text)"/><rect x="10" y="8" width="2.5" height="8" fill="var(--teal-text)"/><rect x="14" y="5" width="2.5" height="11" fill="var(--teal-text)"/></svg>
        <span class="u">Grow</span>
      </h3>
      <ul class="features">
        <li>$550/mo billed annually; $575/mo billed monthly</li>
        <li>CloudLedger Online subscription</li>
        <li>Free accounting setup</li>
        <li>Weekly transaction processing</li>
        <li>Monthly account reconciliation (up to 4 accounts)</li>
        <li>Monthly financial statements by the 10th of the month</li>
        <li>Client portal access for document sharing</li>
        <li>1 Custom Report</li>
        <li>Accounts Payable</li>
        <li>Monthly Scorecard (customized metric tracking for your business)</li>
      </ul>
    </article>
  </div>

  <div class="col col-right">
    <article class="package">
      <h3 class="package-name">
        <svg class="package-icon" viewBox="0 0 22 22"><circle cx="11" cy="11" r="9.5" fill="none" stroke="var(--teal-text)" stroke-width="2"/><path d="M7 12 l3 3 l5 -7" fill="none" stroke="var(--teal-text)" stroke-width="2"/></svg>
        <span class="u">Relax</span> <span class="note">(We've Got This)</span>
      </h3>
      <ul class="features">
        <li>$850/mo billed annually; $875/mo billed monthly</li>
        <li>CloudLedger Online subscription</li>
        <li>Free accounting setup</li>
        <li>Weekly transaction processing</li>
        <li>Monthly account reconciliation (up to 5-10 accounts)</li>
        <li>Monthly financial statements by the 5th of the month</li>
        <li>Client portal access for document sharing</li>
        <li>2 Custom Reports</li>
        <li>Accounts Payable</li>
        <li>Invoicing and accounts receivable</li>
        <li>Weekly Scorecard (customized metric tracking)</li>
      </ul>
    </article>
    <section>
      <h3 class="addons-title">Additional Options</h3>
      <div class="addons">
        <span class="addon-label">Payroll-</span>
        <span class="addon-price">$85/mo<small>(1-10 Employees)</small><br>$175/mo<small>(11-30 Employees)</small></span>
        <span class="addon-label">Sales Tax -</span>
        <span class="addon-price">$30/mo<small>(Per State)</small></span>
        <span class="addon-label">Corporate Taxes-</span>
        <span class="addon-price">$50/mo</span>
        <span class="addon-label">Owner Taxes -</span>
        <span class="addon-price">$25/mo</span>
      </div>
    </section>
  </div>

  <footer class="call-band">Cal Us Today XXXXXXXXX</footer>
</main>
</body>
</html>
```